Furniture Design Website Homepage

Brief as attached- Homepage Design

Silver Heron Furniture is a national retail emporium offering high quality, unique Scandinavian furniture, lighting and accessories. We are the market leader in this space and currently have 2 Showrooms – Melbourne & Sydney.

Most recently our business model has evolved from purely importing premium, one off vintage pieces to a more scalable model of representing brands and manufacturers exclusively out of Scandinavia. These partners manufacture today which ensures us of supply & quality.

We have now started to engage scandinavian designers and/or their families to re-introduce designs that have long gone out of production. These items are put back into production under the silver heron brand, and we own the world wide rights to them.

Please ensure you use the brief files attached and the catalogue images when creating the design.

Target Market(s)

Silver Heron Furniture - where beautiful Scandinavian design meets my modern Australian life.

We want our target audience to chose Scandinavian for their homes & for us to be their brand of choice.

The current perception is that we offer beautiful design but that it doesn’t suit everyone’s home / life / style.

Also that we are more expensive than most.

Industry/Entity Type

Retail

Requirements
Must have
• The colour scheme should be red and white as per the catalogue I attached. We like the look and feel of this site www.roomfondly.example

The furniture is more luxurious, so we need to target the upper market with a nice sleek look that makes the furniture look expensive.

```html
<!DOCTYPE html>
<html lang="en">
<head>
<meta charset="utf-8">
<title>Silver Heron Furniture</title>
<link rel="stylesheet" href="https://fonts.googleapis.com/css2?family=Noto+Sans:wght@400;700&display=swap">
<style>
:root{
  --red:#9b2a10;
  --red-dark:#7d1c0a;
  --maroon:#7b1d24;
  --gold:#f6b21a;
  --cream:#f1f1f1;
  --navy:#253a7a;
  --link-blue:#1a8ad4;
  --teal:#1f7d74;
  --yellow:#ffd400;
  --text:#222;
  --white:#fff;
}
*{box-sizing:border-box;margin:0;padding:0}
html,body{width:1200px;height:1106px;overflow:hidden;background:var(--white);font-family:"Noto Sans",Verdana,sans-serif;color:var(--text)}
.page{position:relative;width:1200px;height:1106px}
.abs{position:absolute}
a{color:inherit}

/* header */
.brand{left:145px;top:56px;display:flex;align-items:center;gap:8px;font-size:26px;font-weight:700;color:#2b2b2b;letter-spacing:-.5px;line-height:30px}
.brand .mark{width:14px;height:14px;background:var(--red)}
.cart{left:904px;top:5px;font-size:12px;line-height:21px;color:#333}
.cart h3{display:flex;align-items:center;gap:4px;font-size:13px;font-weight:700;color:#444}
.cart p{padding-left:4px}
.cart .links a{color:var(--red)}

/* sidebar */
.sidebar{left:141px;top:97px;width:208px;height:920px;background:var(--red);border-radius:4px;color:var(--white)}
.sidebar > *{position:absolute}
.side-title{left:8px;font-size:14px;font-weight:700;line-height:20px}
.search{left:13px;top:44px;display:flex;height:20px;width:186px;background:#fff;border:1px solid #999;border-radius:3px;font-size:11px;color:#222;align-items:center}
.search span{flex:1;padding-left:28px}
.search b{width:28px;border-left:1px solid #aaa;height:100%;display:flex;align-items:center;justify-content:center;font-weight:400;background:#eee}
.rule{left:8px;width:192px;border-top:1px dashed rgba(255,255,255,.3)}
.range{left:12px;top:103px;list-style:none}
.range li{font-size:11px;line-height:21.5px}
.types{left:12px;top:250px;width:190px}
.type-row{display:flex;font-size:11px;line-height:21.5px}
.type-row span{width:70px}
.type-row i{margin-left:7px;width:106px;height:14px;margin-top:4px;background:#fff;border:1px solid #888;position:relative}
.type-row i::after{content:"";position:absolute;right:0;top:0;width:14px;height:12px;background:#e7e7e7;border-left:1px solid #888}
.btn-find{left:43px;top:366px;width:110px;height:20px;background:#f3f3f3;color:var(--red);font-size:12px;text-align:center;line-height:20px;border:1px solid #ccc}
.side-copy{left:9px;top:429px;width:192px;font-size:11px;line-height:17px}
.join{left:9px;top:470px;width:190px;display:flex;height:22px;font-size:11px}
.join span{flex:1;background:#fff;color:#222;padding-left:10px;line-height:22px;border-radius:3px 0 0 3px}
.join b{width:54px;background:var(--teal);text-align:center;line-height:22px;border-radius:0 3px 3px 0}
.privacy{left:10px;top:490px;font-size:11px;line-height:16px;color:var(--yellow)}
.box{left:7px;width:197px;background:#fff;color:#333}
.box-head{background:linear-gradient(var(--red),var(--red-dark));color:#fff;font-size:14px;height:34px;line-height:34px;padding-left:9px;position:relative;border:1px solid #b84a30}
.plus{position:absolute;right:8px;top:8px;width:18px;height:18px;background:#fff;color:var(--red);font-weight:700;line-height:17px;text-align:center;font-size:15px}
.testi{display:flex;gap:6px;padding:8px 5px 6px;height:78px;border-bottom:1px dashed #ccc}
.portrait{width:62px;height:62px;background:linear-gradient(#d9e2ec,#8a98ad);border:1px solid #bbb;flex:none}
.testi h4{font-size:14px;font-weight:400;color:var(--link-blue);line-height:17px}
.testi p{font-size:10.5px;line-height:15px;text-decoration:underline;color:#555}
.cards{display:grid;grid-template-columns:83px 82px;gap:14px 17px;padding:8px 0 8px 6px}
.card{height:54px;border:1px solid #888;display:flex;align-items:center;justify-content:center;font-size:12px;font-weight:700;color:#333;background:#fff}
.card.dark{background:#1d1d3a;color:#fff}

/* nav */
.nav{left:358px;top:97px;width:711px;height:32px;background:var(--red);border-radius:4px;display:flex;align-items:center;padding-left:11px;font-size:12px;color:#fff}
.nav .sep{margin:0 9px}
.intro{left:360px;top:134px;width:710px}
.intro h1{font-size:21px;color:var(--red);font-weight:700;line-height:28px}
.intro p{font-size:10.5px;line-height:16px;margin-top:2px;letter-spacing:.25px}

/* hero */
.hero{left:357px;top:205px;width:712px;height:273px;border:1px solid #bbb;border-radius:4px;overflow:hidden;display:flex;background:#fff}
.hero-photo{width:497px;background:radial-gradient(ellipse at 50% 45%,#c9d9cb 0 42%,#f6f6f4 70%)}
.tiles{flex:1;display:flex;flex-direction:column;gap:8px}
.tile{flex:1;background:var(--maroon);display:flex;align-items:center;gap:6px;padding-left:6px}
.tile .thumb{width:73px;height:48px;background:radial-gradient(ellipse,#c5d6c7 0 50%,#f4f4f2 75%);border:2px solid #fff;flex:none}
.tile h3{font-size:20px;font-weight:400;color:#fff;line-height:24px}
.tile a{font-size:15px;color:var(--gold);text-decoration:none}

/* sections */
.sec-head{left:357px;width:712px;height:34px;background:linear-gradient(var(--red),var(--red-dark));color:#fff;font-size:14px;font-weight:700;line-height:34px;padding-left:9px;border-radius:3px 3px 0 0}
.sec-body{left:357px;width:712px;background:var(--cream);border:1px solid #ddd}
.products{top:531px;height:267px}
.product{position:absolute;top:13px;width:187px}
.product-photo{height:183px;border:1px solid #bbb;background:radial-gradient(ellipse at 50% 50%,#d49a3d 0 32%,#fff 62%)}
.product h4{font-size:13px;color:var(--navy);margin-top:6px;line-height:18px}
.product .price{font-size:10px;margin-top:5px}
.pbtn{position:absolute;right:0;width:70px;height:22px;background:var(--red);color:#fff;font-size:10px;text-align:center;line-height:20px;border:1px solid #5a1505}
.pbtn.detail{top:188px}
.pbtn.add{top:215px}
.divider{position:absolute;top:545px;height:230px;border-left:1px dashed #ccc}
.newsletter{top:860px;height:157px;padding:6px 5px;font-size:12.5px;line-height:17px}
.field{position:absolute;display:flex;align-items:center;font-size:12.5px}
.field span{width:69px}
.field i{width:221px;height:22px;background:#fff;border:1px solid #999;border-radius:2px;margin-left:4px}
.join-btn{position:absolute;left:450px;top:112px;width:165px;height:23px;background:var(--red);color:#fff;text-align:center;line-height:21px;font-size:12px;border:1px solid #5a1505}
.nl-privacy{position:absolute;left:477px;top:137px;font-size:9px;line-height:12px;color:var(--navy);text-decoration:underline}

/* footer */
.footer{left:0;top:1022px;width:1200px;height:84px;background:var(--red);color:#fff}
.f-brand{left:141px;top:40px;font-size:12px;font-weight:700;line-height:16px;color:#fff}
.f-nav{left:235px;top:14px;font-size:11px;line-height:16px;display:flex}
.f-nav .sep{margin:0 11px}
.f-copy{left:234px;top:44px;font-size:11px;line-height:16px}
.social{left:901px;top:10px}
.social h3{font-size:15px;font-weight:700;line-height:20px}
.social .icons{display:flex;gap:10px;margin-top:6px}
.social .icons span{width:32px;height:32px;background:#fff;color:var(--red);border-radius:4px;font-size:15px;font-weight:700;display:flex;align-items:center;justify-content:center}
</style>
</head>
<body>
<div class="page">

  <header>
    <div class="abs brand"><span class="mark"></span>silver heron</div>
    <div class="abs cart">
      <h3><svg width="22" height="20" viewBox="0 0 22 20"><path d="M1 2h4l3 10h10l3-7H7" fill="none" stroke="#1a8ad4" stroke-width="2"/><circle cx="9" cy="16" r="2" fill="#1a8ad4"/><circle cx="17" cy="16" r="2" fill="#1a8ad4"/></svg>Shopping Cart</h3>
      <p>Item &nbsp;: 0</p>
      <p>Total &nbsp;: $0.00</p>
      <p class="links"><a href="#">View Cart</a> | &nbsp;<a href="#">Checkout</a></p>
    </div>
  </header>

  <aside class="abs sidebar">
    <h2 class="side-title" style="top:16px">Product Search</h2>
    <div class="search"><span>Search...</span><b>GO</b></div>
    <div class="rule" style="top:77px"></div>
    <h2 class="side-title" style="top:83px">Browse Our range</h2>
    <ul class="range"><li>Furniture</li><li>Furniture Packages</li><li>Accessories</li><li>Lighting</li><li>Fabric</li></ul>
    <div class="rule" style="top:219px"></div>
    <h2 class="side-title" style="top:224px">View Product By Type</h2>
    <div class="types">
      <div class="type-row"><span>Room</span>:<i></i></div>
      <div class="type-row"><span>Furniture</span>:<i></i></div>
      <div class="type-row"><span>Designers</span>:<i></i></div>
      <div class="type-row"><span>Brands</span>:<i></i></div>
      <div class="type-row"><span>Accessories</span>:<i></i></div>
    </div>
    <span class="btn-find">Find Products</span>
    <div class="rule" style="top:400px"></div>
    <h2 class="side-title" style="top:405px">Keep Up To Date</h2>
    <p class="side-copy">Discover Exclusive offers, Product Previews and much &nbsp;More</p>
    <div class="join"><span>Join Our Newslatter</span><b>Submit</b></div>
    <a class="privacy" href="#" style="top:498px">We Valur Your Privacy</a>
    <div class="rule" style="top:522px"></div>
    <section class="box" style="top:534px;height:192px">
      <div class="box-head">Testimonial<span class="plus">+</span></div>
      <div class="testi"><div class="portrait" role="img" aria-label="Customer portrait"></div><div><h4>Lorem Ipsum</h4><p>Reference site about Lorem Ipsum, giving information</p></div></div>
      <div class="testi" style="border:0"><div class="portrait" role="img" aria-label="Customer portrait"></div><div><h4>Lorem Ipsum</h4><p>Reference site about Lorem Ipsum, giving information</p></div></div>
    </section>
    <section class="box" style="top:742px;height:170px">
      <div class="box-head">Accepted Creadit Card</div>
      <div class="cards">
        <div class="card">Roundpay</div>
        <div class="card">Veltra</div>
        <div class="card dark">Duocard</div>
        <div class="card">Roundpay</div>
      </div>
    </section>
  </aside>

  <nav class="abs nav">
    <span>About Us</span><span class="sep">|</span><span>Furniture Restoration</span><span class="sep">|</span><span>Media</span><span class="sep">|</span><span>FAQ's</span><span class="sep">|</span><span>Malling List</span><span class="sep">&nbsp;|</span><span>Blog</span><span class="sep">|</span><span>Site Search</span><span class="sep">|</span><span>Contact Us</span><span class="sep">|</span><span>Login</span>
  </nav>

  <div class="abs intro">
    <h1>Heading</h1>
    <p>Lorem Ipsum is simply dummy text of the printing and typesetting industry. Lorem Ipsum has been the industry's standard dummy text ever since the 1500sLorem Ipsum is simply dummy text of the printing and typesetting industry. Lorem Ipsum has been the</p>
  </div>

  <section class="abs hero">
    <div class="hero-photo" role="img" aria-label="Pale green tufted two-seat sofa on wooden legs"></div>
    <div class="tiles">
      <div class="tile"><div class="thumb" role="img" aria-label="Sofa thumbnail"></div><div><h3>Furniture</h3><a href="#">View Collection</a></div></div>
      <div class="tile"><div class="thumb" role="img" aria-label="Sofa thumbnail"></div><div><h3>Accessories</h3><a href="#">View Collection</a></div></div>
      <div class="tile"><div class="thumb" role="img" aria-label="Sofa thumbnail"></div><div><h3>Lighting</h3><a href="#">View Collection</a></div></div>
      <div class="tile"><div class="thumb" role="img" aria-label="Sofa thumbnail"></div><div><h3>Furniture</h3><a href="#">View Collection</a></div></div>
    </div>
  </section>

  <div class="abs sec-head" style="top:497px">Silver Heron Recommends</div>
  <section class="abs sec-body products">
    <div class="product" style="left:18px"><div class="product-photo" role="img" aria-label="Tan leather armchair"></div><h4>Product Name</h4><p class="price">$500.00</p><span class="pbtn detail">More Detail</span><span class="pbtn add">Add To Cart</span></div>
    <div class="product" style="left:260px"><div class="product-photo" role="img" aria-label="Tan leather armchair"></div><h4>Product Name</h4><p class="price">$500.00</p><span class="pbtn detail">More Detail</span><span class="pbtn add">Add To Cart</span></div>
    <div class="product" style="left:504px"><div class="product-photo" role="img" aria-label="Tan leather armchair"></div><h4>Product Name</h4><p class="price">$500.00</p><span class="pbtn detail">More Detail</span><span class="pbtn add">Add To Cart</span></div>
  </section>
  <div class="divider" style="left:591px"></div>
  <div class="divider" style="left:833px"></div>

  <div class="abs sec-head" style="top:827px">Join NewsLetter</div>
  <section class="abs sec-body newsletter">
    <p>Lorem Ipsum is simply dummy text of the printing and typesetting industry. Lorem Ipsum has been the Lorem I rem Ipsum is simply dummy text of the printing and typesetting industry. Lorem Ipsum has been the Lorem</p>
    <div class="field" style="left:6px;top:54px"><span>Name</span>:<i></i></div>
    <div class="field" style="left:343px;top:54px"><span>Email</span>:<i></i></div>
    <div class="field" style="left:6px;top:84px"><span>State</span>:<i></i></div>
    <div class="field" style="left:343px;top:84px"><span>Postcode</span>:<i></i></div>
    <span class="join-btn">Join Our News Letter</span>
    <a class="nl-privacy" href="#">We Valur Your Privacy</a>
  </section>

  <footer class="abs footer">
    <div class="abs f-brand">silver heron</div>
    <div class="abs f-nav"><span>About Us</span><span class="sep">|</span><span>Furniture Restoration</span><span class="sep">|</span><span>Media</span><span class="sep">|</span><span>FAQ's</span><span class="sep">|</span><span>Malling List</span><span class="sep">&nbsp;|</span><span>Blog</span><span class="sep">|</span><span>Site Search</span><span class="sep">|</span><span>Contact Us</span></div>
    <p class="abs f-copy">Copyright © &nbsp;All Rights Reserved.</p>
    <div class="abs social">
      <h3>Join In</h3>
      <div class="icons">
        <span aria-label="Friendwall">F</span><span aria-label="Linkwork">L</span><span aria-label="Chirper">C</span><span aria-label="Tubecast">T</span>
      </div>
    </div>
  </footer>

</div>
</body>
</html>
```